24 hour coin operated Brisk Pulse Workout Hall Grand opening.

We are the first of our kind on the planet. I have invented and opened three 24 hour coin operated cardio centers. It's a gym with no weights and no classes. It only has cardio equipment. Imagine a laundromat or a video game arcade, only the machines are treadmills, cross trainers, stair steppers, bikes, etc. my sales person is a coin changer. I have no employees that work in the gym. It's fully automated. I am opening my fourth location and would like to announce its opening, while offering a special pre sale pricing for my tokens. The pre sale pricing is only good until about a week after I open and then the tokens will be regular price. The price is buy 40 tokens get 10 free. My opening day is expected to be Septmebr 14th, so bonus offer ends on the 22nd of Septemebr. I am hoping for a unique design to go along with our unique fitness style.

Target Market(s)

Men and Women from the ages of 14 to 65. all ages really.

Industry/Entity Type

Fitness

Font styles to use
Sans Serif

Colors
fbed22
000000

Requirements
Must have
• Our name and logo B Pulse Workout
• Our FB access name FB:BRISKPULSEWORKOUT
• Must say 24 hours
• Must say worlds first coin operated cardio center.
• Must say grand opening special offer ends Septemebr 22nd
• Phone number: 0958476201
• Must have our address and map:
• No.53, Linsen Rd., Beiyuan Dist., Tainan City 710 (see attached men for map)
Nice to have
• Website: briskpulsewkt.example
Should not have
• Please don't worry about the Chinese characters If I haven't asked you to add them. Sorry, this is to save time for those who haven't been selected.

```html
<!DOCTYPE html>
<html lang="en">
<head>
<meta charset="utf-8">
<title>Brisk Pulse Workout Hall – Grand Opening</title>
<link rel="stylesheet" href="https://fonts.googleapis.com/css2?family=Archivo+Black&family=Montserrat:wght@500;600;700;800&family=Oswald:wght@500;600;700&family=Questrial&display=swap">
<style>
  :root {
    --yellow: #fbed22;
    --black: #000000;
    --ink: #111111;
    --white: #ffffff;
    --grey-light: #f1f1f1;
    --grey-ring: #8a8a8a;
  }
  html, body {
    margin: 0;
    padding: 0;
    overflow: hidden;
    background: var(--white);
  }
  .flyer {
    position: relative;
    width: 848px;
    height: 1200px;
    overflow: hidden;
    background: radial-gradient(circle at 50% 78%, var(--white) 0%, var(--grey-light) 70%);
    font-family: "Montserrat", sans-serif;
    color: var(--ink);
  }
  .flyer p, .flyer h1 { margin: 0; }
  .flyer-shapes { position: absolute; inset: 0; }

  .brand {
    position: absolute;
    left: 40px;
    top: 62px;
    display: flex;
    align-items: center;
    gap: 12px;
  }
  .brand-dot {
    width: 30px;
    height: 30px;
    border-radius: 50%;
    background: var(--black);
  }
  .brand-name {
    font-weight: 800;
    font-size: 24px;
    line-height: 1.05;
    color: var(--black);
    text-transform: uppercase;
    width: 180px;
  }
  .hours {
    position: absolute;
    left: 40px;
    top: 132px;
    font-family: "Oswald", sans-serif;
    font-weight: 700;
    font-size: 26px;
    line-height: 1;
    color: var(--black);
  }
  .fb-name {
    position: absolute;
    left: 40px;
    top: 166px;
    font-family: "Montserrat", sans-serif;
    font-weight: 700;
    font-size: 14px;
    line-height: 1;
    color: var(--black);
  }

  .tagline {
    position: absolute;
    left: 30px;
    top: 676px;
    font-family: "Questrial", sans-serif;
    font-size: 33px;
    line-height: 1;
    -webkit-text-stroke: 0.5px var(--ink);
    white-space: nowrap;
  }
  .headline-name {
    position: absolute;
    left: 28px;
    top: 722px;
    font-weight: 700;
    font-size: 58px;
    line-height: 1;
    white-space: nowrap;
  }
  .headline-location {
    position: absolute;
    left: 30px;
    top: 796px;
    font-family: "Archivo Black", sans-serif;
    font-size: 25px;
    line-height: 1;
    white-space: nowrap;
  }
  .opening-day {
    position: absolute;
    left: 30px;
    top: 836px;
    font-family: "Oswald", sans-serif;
    font-weight: 600;
    font-size: 34px;
    line-height: 1.2;
    letter-spacing: -0.5px;
    white-space: nowrap;
  }
  .call {
    position: absolute;
    left: 592px;
    top: 740px;
    font-family: "Oswald", sans-serif;
    font-weight: 700;
    font-size: 32px;
    line-height: 1.25;
  }

  .offer-note {
    position: absolute;
    left: 50px;
    top: 930px;
    width: 490px;
    font-weight: 500;
    font-size: 13px;
    line-height: 1.35;
  }
  .offer-title {
    position: absolute;
    left: 50px;
    top: 972px;
    font-weight: 700;
    font-size: 31px;
    line-height: 1.1;
    white-space: nowrap;
  }
  .offer-deadline {
    position: absolute;
    left: 50px;
    top: 1012px;
    font-family: "Oswald", sans-serif;
    font-weight: 700;
    font-size: 48px;
    line-height: 1.1;
    white-space: nowrap;
  }

  .footer {
    position: absolute;
    left: 0;
    right: 0;
    bottom: 0;
    height: 64px;
    background: var(--black);
    color: var(--white);
    display: flex;
    align-items: center;
    justify-content: space-between;
    padding: 0 30px;
    box-sizing: border-box;
    font-weight: 600;
  }
  .footer-item { display: flex; align-items: center; gap: 8px; }
  .footer-address { font-size: 16px; }
  .footer-web { font-size: 19px; letter-spacing: 1px; }
  .footer-icon { width: 18px; height: 18px; }
</style>
</head>
<body>
<div class="flyer">

  <svg class="flyer-shapes" width="848" height="1200" viewBox="0 0 848 1200">
    <defs>
      <linearGradient id="heroTone" x1="0" y1="0" x2="1" y2="1">
        <stop offset="0" stop-color="#d8d2cb"/>
        <stop offset="0.45" stop-color="#8f7466"/>
        <stop offset="1" stop-color="#2a2f3a"/>
      </linearGradient>
      <linearGradient id="classTone" x1="0" y1="0" x2="0" y2="1">
        <stop offset="0" stop-color="#e7e3dd"/>
        <stop offset="0.6" stop-color="#b58f78"/>
        <stop offset="1" stop-color="#7d6a5c"/>
      </linearGradient>
      <linearGradient id="gymTone" x1="0" y1="0" x2="1" y2="1">
        <stop offset="0" stop-color="#d9dde2"/>
        <stop offset="0.5" stop-color="#8c96a3"/>
        <stop offset="1" stop-color="#4d5560"/>
      </linearGradient>
      <path id="tokenArc" d="M -112 30 A 116 116 0 0 1 88 -76"/>
    </defs>

    <path class="header-field" fill="var(--yellow)"
          d="M0 0 H848 V620 C700 580 520 560 380 560 L0 560 Z"/>

    <path class="hero-photo" role="img" aria-label="Photo of women training on suspension straps in a gym"
          fill="url(#heroTone)"
          d="M330 0 H848 V640 C720 600 560 568 380 566 C290 470 250 340 270 200 C282 110 300 50 330 0 Z"/>

    <path class="swoosh-black" fill="var(--black)"
          d="M360 566 C560 566 720 600 848 640 V690 C720 645 560 604 340 596 Z"/>
    <path class="swoosh-yellow" fill="var(--yellow)"
          d="M340 596 C560 604 720 645 848 690 V708 C720 664 560 620 330 610 Z"/>
    <path class="hero-edge" fill="none" stroke="var(--black)" stroke-width="8"
          d="M330 0 C300 50 282 110 270 200 C250 340 290 470 380 566"/>

    <rect class="location-map" role="img" aria-label="Street map showing the Linsen Rd. location"
          x="40" y="192" width="200" height="118" rx="8" fill="#e9e4c2" stroke="var(--black)" stroke-width="3"/>

    <circle cx="105" cy="448" r="112" fill="var(--black)"/>
    <circle cx="105" cy="448" r="104" fill="var(--white)"/>
    <circle class="class-photo" role="img" aria-label="Photo of a group cardio class in a studio"
            cx="105" cy="448" r="96" fill="url(#classTone)"/>

    <circle cx="335" cy="532" r="108" fill="var(--grey-ring)"/>
    <circle cx="335" cy="532" r="100" fill="var(--white)"/>
    <circle class="equipment-photo" role="img" aria-label="Photo of treadmills lined up in the workout hall"
            cx="335" cy="532" r="92" fill="url(#gymTone)"/>

    <rect class="offer-band" x="30" y="915" width="788" height="172" rx="22" fill="var(--yellow)"/>

    <g class="token-burst" transform="translate(702 992)">
      <polygon fill="var(--black)" points="140,0 120.5,19 133.1,43.3 108.7,55.4 113.3,82.3 86.3,86.3 82.3,113.3 55.4,108.7 43.3,133.1 19,120.5 0,140 -19,120.5 -43.3,133.1 -55.4,108.7 -82.3,113.3 -86.3,86.3 -113.3,82.3 -108.7,55.4 -133.1,43.3 -120.5,19 -140,0 -120.5,-19 -133.1,-43.3 -108.7,-55.4 -113.3,-82.3 -86.3,-86.3 -82.3,-113.3 -55.4,-108.7 -43.3,-133.1 -19,-120.5 0,-140 19,-120.5 43.3,-133.1 55.4,-108.7 82.3,-113.3 86.3,-86.3 113.3,-82.3 108.7,-55.4 133.1,-43.3 120.5,-19"/>
      <text fill="var(--yellow)" font-family="Oswald, sans-serif" font-weight="600" font-size="14" letter-spacing="1">
        <textPath href="#tokenArc">PRE SALE PRICING FOR TOKEN</textPath>
      </text>
      <text x="0" y="-30" text-anchor="middle" fill="var(--white)" font-family="Oswald, sans-serif" font-weight="600" font-size="38">Buy</text>
      <text x="0" y="20" text-anchor="middle" fill="var(--white)" font-family="Oswald, sans-serif" font-weight="700" font-size="44">40 tokens</text>
      <text x="0" y="60" text-anchor="middle" fill="var(--yellow)" font-family="Oswald, sans-serif" font-weight="600" font-size="30">Get 10 free</text>
    </g>
  </svg>

  <div class="brand">
    <span class="brand-dot"></span>
    <span class="brand-name">Brisk Pulse Workout</span>
  </div>
  <p class="hours">OPEN 24 HOURS</p>
  <p class="fb-name">FB:BRISKPULSEWORKOUT</p>

  <p class="tagline">Worlds first coin operated cardio center</p>
  <h1 class="headline-name">Brisk Pulse</h1>
  <p class="headline-location">WORKOUT HALL 4TH LOCATION</p>
  <p class="opening-day">Opening Day - 14th, Septmebr</p>

  <div class="call">
    <div class="call-label">CALL US:</div>
    <div class="call-number">0958476201</div>
  </div>

  <p class="offer-note">Pre sale pricing is only good until about a week after I open and then the tokens will be regular price.</p>
  <p class="offer-title">Grand opening special offer</p>
  <p class="offer-deadline">ENDS SEPTEMEBR 22ND</p>

  <footer class="footer">
    <span class="footer-item footer-address">
      <svg class="footer-icon" viewBox="0 0 24 24" aria-hidden="true"><path fill="var(--yellow)" d="M12 2a7 7 0 0 0-7 7c0 5 7 13 7 13s7-8 7-13a7 7 0 0 0-7-7zm0 9.5A2.5 2.5 0 1 1 12 6.5a2.5 2.5 0 0 1 0 5z"/></svg>
      No.53, Linsen Rd., Beiyuan Dist., Tainan City 710
    </span>
    <span class="footer-item footer-web">
      <svg class="footer-icon" viewBox="0 0 24 24" aria-hidden="true"><circle cx="12" cy="12" r="10" fill="var(--yellow)"/><path d="M2 12h20M12 2c3 3 3 17 0 20M12 2c-3 3-3 17 0 20" stroke="var(--black)" stroke-width="1.4" fill="none"/></svg>
      www.briskpulsewkt.example
    </span>
  </footer>

</div>
</body>
</html>
```